Maple Crest Staffing Agency

I need to make a brochure/catalogue that represent our company, telling our clients what we do, our values, fields of industry that we taken care of, so they know who we are, what we did, and how we do it.
I do have a logo and simple brochure design before that i really need to upgrade (i will give it as an example on this attachment).

What I want in the new design is :
1. More pictures and little bit of explanation in each industry we work with.
2. Attractive design that make people LOOK at the brochure and not just throw it in the trash.
3. Still use the combination color of the company logo itself, which is Golden Brown.

```html
<!DOCTYPE html>
<html lang="en">
<head>
<meta charset="utf-8">
<title>Maple Crest Staffing Agency – Trifold Brochure</title>
<link rel="stylesheet" href="https://fonts.googleapis.com/css2?family=Poppins:wght@400;500;600;700;800&family=Montserrat:wght@400;500&display=swap">
<style>
:root{
  --backdrop:#7b807f;
  --ink:#141414;
  --panel:#1c1c1c;
  --panel-deep:#0f0f0f;
  --gold:#c9a24a;
  --gold-light:#e6c97a;
  --gold-deep:#a07b2f;
  --pill:#b08a3e;
  --white:#ffffff;
  --paper-text:#222222;
}
*{margin:0;padding:0;box-sizing:border-box}
html,body{width:1200px;height:2400px;overflow:hidden}
body{background:var(--backdrop);font-family:"Montserrat",sans-serif;color:var(--white);position:relative}
.spread{position:absolute;left:30px;width:1140px;height:880px;background:var(--panel);box-shadow:0 6px 18px rgba(0,0,0,.35);overflow:hidden}
.spread--outside{top:280px}
.spread--inside{top:1200px}
.panel{position:absolute;top:0;width:380px;height:880px;overflow:hidden}
.panel--1{left:0}.panel--2{left:380px}.panel--3{left:760px}
.panel--shade{background:linear-gradient(180deg,#1e1e1e,#141414)}
.panel--dark{background:linear-gradient(180deg,#171717,#0d0d0d)}
.photo{position:absolute}
.overlay{position:absolute;left:0;top:0;pointer-events:none}
.heading{position:absolute;font-family:"Poppins",sans-serif;font-weight:700;font-size:19px;color:var(--gold);letter-spacing:.2px}
.heading--rule::after{content:"";display:block;width:102px;height:2px;background:var(--gold);margin-top:6px}
.heading--dark{color:var(--paper-text);font-weight:800}
.copy{position:absolute;font-size:11.2px;line-height:13.9px;text-align:justify;color:#eeeeee}
.copy--dark{color:var(--paper-text);text-align:left}

/* outside spread */
.call-label{position:absolute;top:62px;width:100%;text-align:center;font-family:"Poppins",sans-serif;font-size:19px;letter-spacing:.5px}
.phone-pill{position:absolute;left:52px;top:100px;width:276px;height:56px;border-radius:10px;background:var(--pill);font-family:"Poppins",sans-serif;font-weight:700;font-size:31px;letter-spacing:1px;text-align:center;line-height:56px}
.locations{position:absolute;left:52px;top:316px;width:300px;display:grid;grid-template-columns:165px 135px;row-gap:10px}
.location{display:flex;align-items:center;gap:8px;font-size:14px}
.location svg{flex:none}
.contact{position:absolute;width:100%;text-align:center;font-size:14px}
.contact svg{display:block;margin:0 auto 6px}
.contact .rule{display:block;width:108px;height:1.5px;background:var(--gold);margin:10px auto 0}
.brand-name{position:absolute;width:100%;text-align:center;font-family:"Poppins",sans-serif;font-weight:600;color:var(--gold)}
.brand-name--large{top:78px;font-size:27px;letter-spacing:.5px}
.brand-name--small{top:790px;font-size:15px}
.brand-dot{display:inline-block;width:12px;height:12px;border-radius:50%;background:var(--gold);margin-right:8px;vertical-align:1px}
.tagline{position:absolute;top:672px;width:100%;text-align:center;font-family:"Poppins",sans-serif;font-weight:700;font-size:32px;line-height:41px;color:var(--gold)}
.site{position:absolute;top:826px;width:100%;text-align:center;font-size:14px;letter-spacing:.4px}

/* inside spread */
.story-band{position:absolute;left:0;top:0;width:760px;height:262px;background:var(--white)}
.industries{position:absolute;left:0;top:462px;width:380px}
.industry-row{display:flex;justify-content:center;gap:30px}
.industry-row + .industry-row{margin-top:20px;gap:38px}
.industry{width:70px;text-align:center;font-family:"Poppins",sans-serif;font-weight:600;font-size:10px;letter-spacing:.1px}
.industry svg{display:block;margin:0 auto 8px}
.row-wide .industry{width:92px}
.closing{position:absolute;left:28px;font-family:"Poppins",sans-serif}
.closing--lead{top:676px;font-size:21px;line-height:26px;font-weight:400;color:var(--white)}
.closing--gold{top:756px;font-size:35px;line-height:43px;font-weight:700;color:var(--gold)}
</style>
</head>
<body>

<!-- OUTSIDE SPREAD -->
<section class="spread spread--outside" aria-label="Brochure outside">
  <article class="panel panel--1 panel--shade">
    <div class="photo" role="img" aria-label="Hand touching a glowing person icon within a network of connected people icons" style="left:0;top:0;width:380px;height:200px;background:linear-gradient(120deg,#f2f2f2 0%,#d9d6d2 40%,#6b5344 70%,#3a2f2a 100%)"></div>
    <svg class="overlay" width="380" height="400" viewBox="0 0 380 400">
      <defs><linearGradient id="goldA" x1="0" x2="0" y1="0" y2="1"><stop offset="0" stop-color="#e6c97a"/><stop offset="1" stop-color="#a07b2f"/></linearGradient></defs>
      <polygon points="0,200 108,200 198,300 288,200 380,200 380,400 0,400" fill="#1c1c1c"/>
      <polyline points="0,202 118,202 198,334 278,202 380,202" fill="none" stroke="url(#goldA)" stroke-width="8" stroke-linejoin="miter"/>
    </svg>
    <h2 class="heading heading--rule" style="left:32px;top:348px">ABOUT US</h2>
    <p class="copy" style="left:32px;top:392px;width:320px">With more than 18 years of experience Maple Crest Staffing provided staffing services to a wide array of locations, all throughout Pennsylvania. Through the last few years we have expanded to 5 other states including New York, New Jersey, Delaware, Virginia and Georgia. Our ethics are a critical building block of our business. Our own success is based on adherence to the highest ethical standards; long-term client relationships, the ability to identify top candidates, and the high-quality professional development of Maple Crest Staffing professionals protecting the confidentiality and interests of clients and candidates.</p>
    <h2 class="heading heading--rule" style="left:32px;top:628px">WHY US?</h2>
    <p class="copy" style="left:32px;top:672px;width:320px">With more than 18 years of experience Maple Crest Staffing provided staffing services to a wide array of locations, all throughout Pennsylvania. Through the last few years we have expanded to 5 other states including New York, New Jersey, Delaware, Virginia and Georgia. Our ethics are a critical building block of our business. Our own success is based on adherence to the highest ethical standards; long-term client relationships, the ability to identify top candidates, and the high-quality professional development of Maple Crest Staffing professionals protecting the confidentiality and interests of clients and candidates.</p>
  </article>

  <article class="panel panel--2 panel--dark">
    <p class="call-label">CALL US TODAY</p>
    <p class="phone-pill">555-014-2290</p>
    <div class="photo" role="img" aria-label="Blurred warehouse interior with shelving and boxes" style="left:0;top:200px;width:380px;height:310px;background:linear-gradient(180deg,#3a2a1e 0%,#4d3826 45%,#2a2119 100%)"></div>
    <h2 class="heading heading--rule" style="left:0;top:266px;width:380px;text-align:center;font-size:18px">OUR LOCATION</h2>
    <div class="locations">
      <div class="location"><svg width="34" height="34" viewBox="0 0 34 34"><circle cx="17" cy="17" r="15.5" fill="none" stroke="#fff" stroke-width="2"/><path d="M17 8a6 6 0 0 1 6 6c0 4.5-6 11-6 11s-6-6.5-6-11a6 6 0 0 1 6-6z" fill="#fff"/><circle cx="17" cy="14" r="2.2" fill="#1c1c1c"/></svg>New York</div>
      <div class="location"><svg width="34" height="34" viewBox="0 0 34 34"><circle cx="17" cy="17" r="15.5" fill="none" stroke="#fff" stroke-width="2"/><path d="M17 8a6 6 0 0 1 6 6c0 4.5-6 11-6 11s-6-6.5-6-11a6 6 0 0 1 6-6z" fill="#fff"/><circle cx="17" cy="14" r="2.2" fill="#1c1c1c"/></svg>Delaware</div>
      <div class="location"><svg width="34" height="34" viewBox="0 0 34 34"><circle cx="17" cy="17" r="15.5" fill="none" stroke="#fff" stroke-width="2"/><path d="M17 8a6 6 0 0 1 6 6c0 4.5-6 11-6 11s-6-6.5-6-11a6 6 0 0 1 6-6z" fill="#fff"/><circle cx="17" cy="14" r="2.2" fill="#1c1c1c"/></svg>Pensylvania</div>
      <div class="location"><svg width="34" height="34" viewBox="0 0 34 34"><circle cx="17" cy="17" r="15.5" fill="none" stroke="#fff" stroke-width="2"/><path d="M17 8a6 6 0 0 1 6 6c0 4.5-6 11-6 11s-6-6.5-6-11a6 6 0 0 1 6-6z" fill="#fff"/><circle cx="17" cy="14" r="2.2" fill="#1c1c1c"/></svg>Verginia</div>
      <div class="location"><svg width="34" height="34" viewBox="0 0 34 34"><circle cx="17" cy="17" r="15.5" fill="none" stroke="#fff" stroke-width="2"/><path d="M17 8a6 6 0 0 1 6 6c0 4.5-6 11-6 11s-6-6.5-6-11a6 6 0 0 1 6-6z" fill="#fff"/><circle cx="17" cy="14" r="2.2" fill="#1c1c1c"/></svg>New jersey</div>
      <div class="location"><svg width="34" height="34" viewBox="0 0 34 34"><circle cx="17" cy="17" r="15.5" fill="none" stroke="#fff" stroke-width="2"/><path d="M17 8a6 6 0 0 1 6 6c0 4.5-6 11-6 11s-6-6.5-6-11a6 6 0 0 1 6-6z" fill="#fff"/><circle cx="17" cy="14" r="2.2" fill="#1c1c1c"/></svg>Georgia</div>
    </div>
    <div class="overlay" style="top:506px;width:380px;height:6px;background:linear-gradient(90deg,#a07b2f,#e6c97a,#a07b2f)"></div>
    <p class="contact" style="top:540px"><svg width="16" height="12" viewBox="0 0 16 12"><rect x="0.5" y="0.5" width="15" height="11" fill="#c9a24a"/><polyline points="0.5,0.5 8,7 15.5,0.5" fill="none" stroke="#141414" stroke-width="1.3"/></svg>info@maplecreststaffing.com<span class="rule"></span></p>
    <p class="contact" style="top:606px"><svg width="12" height="16" viewBox="0 0 12 16"><path d="M6 0a6 6 0 0 1 6 6c0 4-6 10-6 10S0 10 0 6a6 6 0 0 1 6-6z" fill="#c9a24a"/><circle cx="6" cy="6" r="2" fill="#141414"/></svg>42 Orchard Ln, suite 210<br>Brookfield. NJ 08000<span class="rule"></span></p>
    <p class="contact" style="top:700px"><svg width="15" height="15" viewBox="0 0 16 16"><circle cx="8" cy="8" r="7" fill="none" stroke="#c9a24a" stroke-width="1.6"/><ellipse cx="8" cy="8" rx="3" ry="7" fill="none" stroke="#c9a24a" stroke-width="1.3"/><line x1="1" y1="8" x2="15" y2="8" stroke="#c9a24a" stroke-width="1.3"/></svg>www.maplecreststaffing.com<span class="rule"></span></p>
    <p class="brand-name brand-name--small"><span class="brand-dot"></span>MAPLE CREST Inc.</p>
  </article>

  <article class="panel panel--3 panel--shade">
    <p class="brand-name brand-name--large"><span class="brand-dot"></span>MAPLE CREST Inc.</p>
    <div class="photo" role="img" aria-label="Smiling businessman in shirt and striped tie standing in a warehouse" style="left:0;top:200px;width:380px;height:320px;background:linear-gradient(180deg,#5a4430 0%,#8a7058 40%,#c9cdd8 75%,#3c3a42 100%)"></div>
    <svg class="overlay" width="380" height="700" viewBox="0 0 380 700">
      <defs><linearGradient id="goldB" x1="0" x2="0" y1="0" y2="1"><stop offset="0" stop-color="#e6c97a"/><stop offset="1" stop-color="#a07b2f"/></linearGradient></defs>
      <polygon points="0,508 100,508 190,606 280,508 380,508 380,700 0,700" fill="#1c1c1c"/>
      <polyline points="0,510 110,510 190,642 270,510 380,510" fill="none" stroke="url(#goldB)" stroke-width="8"/>
    </svg>
    <h1 class="tagline">WE MAKE<br>FINDING GREAT<br>PEOPLE EASY</h1>
    <p class="site">www.maplecreststaffing.com</p>
  </article>
</section>

<!-- INSIDE SPREAD -->
<section class="spread spread--inside" aria-label="Brochure inside">
  <div class="story-band"></div>
  <div class="photo" role="img" aria-label="Smiling hotel housekeeper with a service cart in a hotel corridor" style="left:330px;top:0;width:430px;height:262px;background:linear-gradient(90deg,#ffffff 0%,#dfe4ee 25%,#b37a4a 60%,#7a2a1e 85%,#3d2a20 100%)"></div>
  <h2 class="heading heading--dark heading--rule" style="left:27px;top:56px">OUR STORY</h2>
  <p class="copy copy--dark" style="left:27px;top:100px;width:290px">With more than 18 years of experience Maple Crest Staffing has provided staffing services all throughout Pennsylvania, New York, New Jersey, Delaware, Virginia &amp; Georgia.<br><br>Our success is based on our unique ability to identify top candidates and the high-quality professional development of our candidates.</p>

  <article class="panel panel--1" style="top:262px;height:618px;background:#141414">
    <div class="photo" role="img" aria-label="Smiling casino dealer in vest and bow tie at a gaming table" style="left:27px;top:41px;width:323px;height:327px;background:linear-gradient(135deg,#e8e8e8 0%,#bdbdbd 40%,#2a2a2a 70%,#6a1e1e 100%)"></div>
    <h2 class="heading heading--rule" style="left:27px;top:398px">OUR CULTURE</h2>
    <p class="copy" style="left:27px;top:444px;width:323px">Maple Crest Staffing believes in equal opportunity for all, regardless of gender, race, ethic, origin, religion, or handicap. The staffing policies and practices of Maple Crest Staffing for our organization, our clients and candidates are fully non-discriminatory. Our employees are our most valuable asset. We strive to create a work environment of professionalism, trust and respect that will continuously provide our staff with motivation, challenge, and professional growth to aim our most important goal; CLIENT SATISFACTION.</p>
  </article>

  <article class="panel panel--2" style="top:262px;height:618px;background:#141414">
    <div class="photo" role="img" aria-label="Group of workers in uniforms of different trades" style="left:24px;top:408px;width:336px;height:170px;background:linear-gradient(180deg,#f4f4f4 0%,#c9b8a4 50%,#6d6258 100%)"></div>
  </article>

  <svg class="overlay" width="760" height="420" viewBox="0 0 760 420">
    <defs><linearGradient id="goldC" x1="0" x2="0" y1="0" y2="1"><stop offset="0" stop-color="#e6c97a"/><stop offset="1" stop-color="#a07b2f"/></linearGradient></defs>
    <polygon points="380,262 432,262 510,360 588,262 760,262 760,420 380,420" fill="#141414"/>
    <polyline points="0,264 442,264 510,400 578,264 760,264" fill="none" stroke="url(#goldC)" stroke-width="8"/>
  </svg>

  <div class="panel panel--2" style="background:none">
    <h2 class="heading heading--rule" style="left:0;top:420px;width:380px;text-align:center;font-size:18px">INDUSTRIES WE SERVE</h2>
    <div class="industries" style="top:470px">
      <div class="industry-row">
        <div class="industry"><svg width="56" height="56" viewBox="0 0 56 56"><circle cx="28" cy="28" r="26" fill="none" stroke="#c9a24a" stroke-width="2.5"/><path d="M16 26 28 17 40 26V39H16Z" fill="#c9a24a"/><rect x="21" y="29" width="14" height="10" fill="#141414"/><line x1="21" y1="33" x2="35" y2="33" stroke="#c9a24a" stroke-width="1.5"/></svg>WAREHOUSING</div>
        <div class="industry"><svg width="56" height="56" viewBox="0 0 56 56"><circle cx="28" cy="28" r="26" fill="none" stroke="#c9a24a" stroke-width="2.5"/><rect x="18" y="16" width="20" height="24" fill="#c9a24a"/><g fill="#141414"><rect x="21" y="19" width="4" height="4"/><rect x="31" y="19" width="4" height="4"/><rect x="21" y="26" width="4" height="4"/><rect x="31" y="26" width="4" height="4"/><rect x="26" y="33" width="4" height="7"/></g></svg>HOTEL</div>
        <div class="industry"><svg width="56" height="56" viewBox="0 0 56 56"><circle cx="28" cy="28" r="26" fill="none" stroke="#c9a24a" stroke-width="2.5"/><rect x="14" y="22" width="14" height="14" rx="2" fill="#c9a24a" transform="rotate(-12 21 29)"/><rect x="28" y="20" width="14" height="14" rx="2" fill="#c9a24a" transform="rotate(14 35 27)"/><g fill="#141414"><circle cx="19" cy="27" r="1.6"/><circle cx="23" cy="31" r="1.6"/><circle cx="33" cy="25" r="1.6"/><circle cx="37" cy="29" r="1.6"/></g></svg>CASINO</div>
        <div class="industry"><svg width="56" height="56" viewBox="0 0 56 56"><circle cx="28" cy="28" r="26" fill="none" stroke="#c9a24a" stroke-width="2.5"/><rect x="14" y="34" width="20" height="5" rx="2.5" fill="#c9a24a"/><rect x="17" y="27" width="12" height="7" fill="#c9a24a"/><polyline points="29,28 36,18 41,26" fill="none" stroke="#c9a24a" stroke-width="2.5"/><path d="M38 26h6l-2 6h-4z" fill="#c9a24a"/></svg>LANDFILL</div>
      </div>
      <div class="industry-row row-wide">
        <div class="industry"><svg width="56" height="56" viewBox="0 0 56 56"><circle cx="28" cy="28" r="26" fill="none" stroke="#c9a24a" stroke-width="2.5"/><rect x="13" y="20" width="19" height="14" fill="#c9a24a"/><path d="M32 24h6l5 5v5H32Z" fill="#c9a24a"/><circle cx="19" cy="36" r="3" fill="#c9a24a" stroke="#141414" stroke-width="1.5"/><circle cx="37" cy="36" r="3" fill="#c9a24a" stroke="#141414" stroke-width="1.5"/></svg>TRANSPORTATION</div>
        <div class="industry"><svg width="56" height="56" viewBox="0 0 56 56"><circle cx="28" cy="28" r="26" fill="none" stroke="#c9a24a" stroke-width="2.5"/><rect x="19" y="15" width="18" height="26" fill="#c9a24a"/><g stroke="#141414" stroke-width="1.6"><line x1="22" y1="21" x2="34" y2="21"/><line x1="22" y1="25" x2="34" y2="25"/><line x1="22" y1="29" x2="34" y2="29"/><line x1="22" y1="33" x2="31" y2="33"/></g></svg>PAPER MAILING</div>
        <div class="industry"><svg width="56" height="56" viewBox="0 0 56 56"><circle cx="28" cy="28" r="26" fill="none" stroke="#c9a24a" stroke-width="2.5"/><g stroke="#c9a24a" stroke-width="2.2" fill="none" stroke-linecap="round"><line x1="20" y1="15" x2="20" y2="23"/><line x1="24" y1="15" x2="24" y2="23"/><path d="M18 15v6a4 4 0 0 0 8 0v-6"/><line x1="22" y1="25" x2="22" y2="41"/><path d="M34 41V15c-4 3-5 9-5 14h5"/></g></svg>FOOD HANDLING</div>
      </div>
    </div>
  </div>

  <article class="panel panel--3" style="background:linear-gradient(180deg,#181818,#0e0e0e)">
    <h2 class="heading heading--rule" style="left:24px;top:58px">OUR MISSION</h2>
    <p class="copy" style="left:24px;top:102px;width:325px">Maple Crest Staffing is more than a staffing company; we want to become your business partner. We understand that payroll and employee-service overhead can be one of the largest expenses for your business. Through our partnership-network programs Maple Crest Staffing can help you reduce the hard-costs of your business expenses. We take responsibility for all our placed employees, including payroll taxes and benefits allowing you to focus on running your business.</p>
    <div class="photo" role="img" aria-label="Warehouse worker in hard hat and safety vest holding a clipboard" style="left:24px;top:253px;width:325px;height:167px;background:linear-gradient(90deg,#9a7a5c 0%,#d8d2c4 45%,#c9d34a 60%,#8a6a4a 100%)"></div>
    <h2 class="heading heading--rule" style="left:24px;top:446px">OUR PROCESS</h2>
    <p class="copy" style="left:24px;top:490px;width:325px">Our screening process includes a thorough interview with each potential candidate to give us insight into the candidate's previous work history, skills, communication abilities and career goals as well as reference checks with their previous employers.</p>
    <svg class="overlay" width="380" height="880" viewBox="0 0 380 880">
      <defs><linearGradient id="goldD" x1="0" x2="0" y1="0" y2="1"><stop offset="0" stop-color="#e6c97a"/><stop offset="1" stop-color="#a07b2f"/></linearGradient></defs>
      <polygon points="0,610 380,610 380,880 0,880" fill="#0e0e0e"/>
      <polyline points="0,608 186,608 268,738 342,608 380,608" fill="none" stroke="url(#goldD)" stroke-width="8"/>
    </svg>
    <p class="closing closing--lead">CONNECTING<br>OPPERTUNETIES</p>
    <p class="closing closing--gold">WITH TODAY'S<br>TOP TALENTS</p>
  </article>
</section>

</body>
</html>
```